Personal loan pre-approval

We are a credit union sending out pre-approvals for personal loans. I am attaching a letter that we sent out during previous pre-approvals. The fine print needs to be included on the postcard from the letter, but the rest is just a guide. The theme I'm thinking of may be Easy, Cold Hard Cash, but I'm not stuck on it. Thanks.

http://www.brightquarry.net/gallerydetail.aspx?sectionID=143&photoID=104

The cash banner is an example of what I had in mind.

We don't want the actual letter on the postcard, it was meant to be a guide only as to what we are selling. The front page should be explaining that they are pre-approved for a personal loan, say up $10,000, at a rate of 7.99% APR*. It should be mentioned how they are pre-approved, which means no credit check, no proof of income needed. Somewhere, either on the front or the back, needs to be the fine print in a discreet fashion. look at the link I provide for some guidance. Thanks!
Updates

Industry/Entity Type

Union

Requirements
Must have
• Must have fine print on postcard that is on example letter.
Should not have
• Should not have the entire letter on the postcard

```html
<!DOCTYPE html>
<html lang="en">
<head>
<meta charset="utf-8">
<title>Personal Loan Pre-Approval Postcard</title>
<link rel="stylesheet" href="https://fonts.googleapis.com/css2?family=Libre+Caslon+Text:wght@400;700&family=Quicksand:wght@400&family=Oswald:wght@600&family=Crimson+Text&display=swap">
<style>
  :root {
    --lavender-light: #d4d5ea;
    --lavender-mid: #9a9dc8;
    --lavender-deep: #656aa3;
    --navy: #26357d;
    --ink: #111111;
    --band-black: #000000;
    --gold: #e6d256;
    --gold-soft: #f1d88a;
    --red: #e1232b;
    --white: #ffffff;
  }
  * { margin: 0; padding: 0; box-sizing: border-box; }
  html, body { width: 1200px; height: 776px; overflow: hidden; background: var(--white); }
  .postcard { position: relative; width: 1200px; height: 776px; background: var(--white); }

  .header-band {
    position: absolute; left: 0; top: 0; width: 1005px; height: 192px;
    background: linear-gradient(100deg, var(--lavender-light) 0%, #b7b9db 35%, #8d91c0 70%, var(--lavender-deep) 100%);
  }
  .brand {
    position: absolute; left: 26px; top: 42px; display: flex; align-items: center; gap: 12px;
  }
  .brand-mark { width: 40px; height: 40px; background: var(--navy); }
  .brand-name {
    font-family: "Libre Caslon Text", Georgia, serif; font-weight: 400;
    font-size: 22px; line-height: 28px; color: var(--navy); letter-spacing: 1px;
  }
  .season-line {
    position: absolute; left: 398px; top: 62px; white-space: nowrap;
    font-family: "Quicksand", "Trebuchet MS", sans-serif; font-weight: 400;
    font-size: 45px; letter-spacing: 0.5px; color: var(--white);
    -webkit-text-stroke: 1.5px var(--red);
  }

  .headline-band {
    position: absolute; left: 0; top: 196px; width: 1200px; height: 141px; background: var(--band-black);
  }
  .headline-main, .headline-sub {
    position: absolute; font-family: "Libre Caslon Text", Georgia, serif; font-weight: 400; white-space: nowrap;
  }
  .headline-main { left: 28px; top: 18px; font-size: 50px; color: var(--gold); }
  .headline-sub { left: 450px; top: 62px; font-size: 48px; color: var(--red); }

  .offer-panel {
    position: absolute; left: 0; top: 340px; width: 796px; height: 436px;
    background: radial-gradient(ellipse 620px 420px at 620px 90px, var(--lavender-light) 0%, var(--lavender-mid) 55%, var(--lavender-deep) 100%);
    clip-path: polygon(0 0, 100% 0, 100% 330px, 518px 330px, 518px 100%, 0 100%);
  }
  .offer-decor { position: absolute; inset: 0; }

  .offer-message {
    position: absolute; left: 40px; top: 24px; width: 470px;
    font-family: "Libre Caslon Text", Georgia, serif; color: var(--navy);
  }
  .offer-message .amount { font-size: 22px; line-height: 30px; font-weight: 700; }
  .offer-message .ease { font-size: 16px; line-height: 24px; margin-top: 4px; }

  .terms {
    position: absolute; left: 40px; top: 113px; width: 470px;
    font-family: "Crimson Text", Georgia, serif; font-size: 16.8px; line-height: 22.5px; color: var(--ink);
  }
  .optout {
    position: absolute; left: 20px; top: 331px; width: 498px;
    font-family: "Crimson Text", Georgia, serif; font-size: 12.6px; line-height: 19px; color: var(--ink);
  }

  .expiry-burst { position: absolute; left: 508px; top: 342px; width: 275px; height: 270px; }
  .expiry-burst svg { position: absolute; inset: 0; width: 100%; height: 100%; }
  .expiry-text {
    position: absolute; inset: 0; display: flex; flex-direction: column; align-items: center; justify-content: center;
    font-family: "Oswald", Impact, sans-serif; font-weight: 600; font-size: 31px; line-height: 43px;
    color: var(--ink); text-align: center; letter-spacing: 0.5px;
  }
  .expiry-text .lead { color: var(--gold-soft); }
  .expiry-text .date { color: var(--white); }
</style>
</head>
<body>
<div class="postcard">
  <header class="header-band">
    <div class="brand">
      <span class="brand-mark"></span>
      <span class="brand-name">Harbor Valley<br>Teachers<br>Credit Union</span>
    </div>
    <p class="season-line">imagine this holiday season!</p>
  </header>

  <section class="headline-band">
    <h1 class="headline-main">Personal Loans...</h1>
    <h2 class="headline-sub">at Unbeatable Rates</h2>
  </section>

  <section class="offer-panel">
    <div class="offer-decor" role="img" aria-label="Soft lavender floral swirl decoration"></div>
    <div class="offer-message">
      <p class="amount">You're pre-approved for up to $10,000 at 7.99% APR*</p>
      <p class="ease">No credit check. No proof of income needed.</p>
    </div>
    <p class="terms">*Maximum unsecured amount is $15,000 including existing loan balances. Existing loan will be paid in full and rolled into new loan at new rate. Minimum advance must be $250. Offer is subject to completion of loan documents and Credit Union membership. See Credit Union for details. Certain restrictions may apply.</p>
    <p class="optout">PRESCREEN &amp; OPT-OUT NOTICE: This “prescreened” offer of credit is based on information in your credit report indicating that you have met certain criteria. This offer is not guaranteed if you do not meet our criteria. You can choose to stop receiving “prescreened” offers of credit from this and other companies by calling toll-free 1-888-555-0142; or write: Meridian Consumer Opt-Out, 410 Ledger Parkway, Cedar Falls, TX 75099.</p>
  </section>

  <div class="expiry-burst">
    <svg viewBox="0 0 100 100" preserveAspectRatio="none" aria-hidden="true">
      <polygon fill="#26357d" points="100,50 92,56.6 97.6,65.5 87.9,69.3 90.5,79.4 80,80 79.4,90.5 69.3,87.9 65.5,97.6 56.6,92 50,100 43.4,92 34.5,97.6 30.7,87.9 20.6,90.5 20,80 9.5,79.4 12.1,69.3 2.4,65.5 8,56.6 0,50 8,43.4 2.4,34.5 12.1,30.7 9.5,20.6 20,20 20.6,9.5 30.7,12.1 34.5,2.4 43.4,8 50,0 56.6,8 65.5,2.4 69.3,12.1 79.4,9.5 80,20 90.5,20.6 87.9,30.7 97.6,34.5 92,43.4"/>
    </svg>
    <div class="expiry-text">
      <span class="lead">SPECIAL</span>
      <span>PRE-APPROVAL</span>
      <span>OFFER EXPIRES</span>
      <span class="date">DEC. 31ST,</span>
      <span class="date">2014!</span>
    </div>
  </div>
</div>
</body>
</html>
```